Maple Ledger Business Card

Colors can be blue, grey and white as you see in the attached logo. Needs to have a spot for name, title, phone, email, address, and website. There also needs to be a spot for an agent's picture.

Contact Information for Business Card

See project description.

Colors

Designer to choose colors to be used in the design.

```html
<!DOCTYPE html>
<html lang="en">
<head>
<meta charset="utf-8">
<title>Maple Ledger Business Card</title>
<link href="https://fonts.googleapis.com/css2?family=Source+Sans+3:wght@400;600;700&display=swap" rel="stylesheet">
<style>
  :root {
    --brand-blue: #2f6fb3;
    --brand-blue-deep: #1f4f94;
    --ink-grey: #3d3f44;
    --roof-grey: #45474c;
    --paper: #ffffff;
    --backdrop: #e7eaec;
    --silver: #d3dbe5;
    --rule: #6a6d73;
    --photo-tone: #c9d3de;
  }
  * { box-sizing: border-box; margin: 0; padding: 0; }
  html, body { width: 1200px; height: 900px; overflow: hidden; }
  body {
    background: var(--backdrop);
    font-family: "Source Sans 3", Arial, sans-serif;
    display: flex;
    align-items: center;
    justify-content: center;
    gap: 40px;
  }
  .card {
    width: 540px;
    height: 309px;
    position: relative;
    overflow: hidden;
    border-radius: 4px;
    box-shadow: 0 10px 24px rgba(0,0,0,0.15);
  }
  /* Front */
  .card-front {
    background: linear-gradient(135deg, var(--brand-blue-deep) 0%, var(--brand-blue) 55%, #3479bb 100%);
    display: flex;
    align-items: center;
    justify-content: center;
  }
  .wordmark {
    display: flex;
    align-items: center;
    gap: 12px;
    font-weight: 600;
    font-size: 38px;
    letter-spacing: 0.04em;
    text-transform: uppercase;
  }
  .card-front .wordmark { color: var(--silver); }
  .wordmark-square {
    width: 20px; height: 20px;
    background: currentColor;
  }
  /* Back */
  .card-back { background: var(--paper); }
  .card-back .wordmark {
    position: absolute;
    left: 36px; top: 44px;
    font-size: 26px;
    color: var(--brand-blue);
  }
  .card-back .wordmark-square { width: 16px; height: 16px; }
  .agent-photo {
    position: absolute;
    right: 30px; top: 22px;
    width: 74px; height: 86px;
    border-radius: 3px;
    background: linear-gradient(180deg, var(--photo-tone) 0%, #aebdcd 100%);
    border: 2px solid var(--brand-blue);
  }
  .divider {
    position: absolute;
    left: 292px; top: 116px;
    width: 1px; height: 92px;
    background: var(--rule);
  }
  .contact-list {
    position: absolute;
    left: 312px; top: 120px;
    list-style: none;
    font-size: 14px;
    color: var(--ink-grey);
  }
  .contact-list li {
    display: flex;
    align-items: center;
    gap: 10px;
    height: 27px;
  }
  .contact-list svg { width: 16px; height: 16px; flex: none; }
  .person {
    position: absolute;
    left: 36px; top: 128px;
    color: var(--ink-grey);
  }
  .person-name {
    font-size: 24px;
    font-weight: 600;
    color: var(--brand-blue);
    line-height: 1.1;
  }
  .person-title {
    font-size: 14px;
    margin-bottom: 10px;
  }
  .person-address {
    font-style: normal;
    font-size: 13px;
    line-height: 1.45;
  }
  .accent-band {
    position: absolute;
    left: 0; right: 0;
    bottom: 26px;
    height: 13px;
    background: var(--brand-blue);
  }
  .band-decoration {
    position: absolute;
    right: 36px;
    bottom: 39px;
    width: 70px;
    height: 28px;
    background: linear-gradient(90deg, var(--roof-grey) 0%, var(--brand-blue) 100%);
  }
</style>
</head>
<body>
  <section class="card card-front" aria-label="Card front">
    <div class="wordmark"><span class="wordmark-square"></span><span>Maple Ledger</span></div>
  </section>

  <section class="card card-back" aria-label="Card back">
    <div class="wordmark"><span class="wordmark-square"></span><span>Maple Ledger</span></div>

    <div class="agent-photo" role="img" aria-label="Agent portrait photo"></div>

    <div class="person">
      <p class="person-name">Dana Whitfield</p>
      <p class="person-title">co-owner</p>
      <address class="person-address">
        Maple Ledger Real Estate<br>
        2185 N Cedar Ave,<br>
        Suite B Millbrook, OH 43210
      </address>
    </div>

    <span class="divider"></span>

    <ul class="contact-list">
      <li>
        <svg viewBox="0 0 16 16" aria-hidden="true"><path fill="#2f6fb3" d="M2 6c0-2 2-3 6-3s6 1 6 3v1h-3V5.5H5V7H2zM4 8h8l2 5H2z"/><circle cx="8" cy="10.5" r="1.5" fill="#fff"/></svg>
        <span>(555) 014-2276</span>
      </li>
      <li>
        <svg viewBox="0 0 16 16" aria-hidden="true"><rect x="1" y="3" width="14" height="10" fill="#2f6fb3"/><path d="M1.5 3.5 8 9l6.5-5.5M1.5 12.5 6 7.5M14.5 12.5 10 7.5" stroke="#fff" stroke-width="1" fill="none"/></svg>
        <span>info@mapleledgerre.com</span>
      </li>
      <li>
        <svg viewBox="0 0 16 16" aria-hidden="true"><g fill="none" stroke="#2f6fb3" stroke-width="1.2"><circle cx="8" cy="8" r="6.5"/><ellipse cx="8" cy="8" rx="3" ry="6.5"/><path d="M1.5 8h13M2.5 4.8h11M2.5 11.2h11"/></g></svg>
        <span>www.mapleledgerre.com</span>
      </li>
    </ul>

    <div class="band-decoration" role="img" aria-label="Decorative house roof rising from the stripe"></div>
    <span class="accent-band"></span>
  </section>
</body>
</html>
```